Business card for consulting firm

We need a double-sided business card for consulting firm, VantoriX. The card should be professional but also creative and visually interesting.

Target Market(s)

Engineering and technology; transport industries; safety critical / heavy industry.

Contact Information for Business Card

See attached file with details.

Font styles to use
Sans Serif

```html
<!DOCTYPE html>
<html lang="en">
<head>
<meta charset="utf-8">
<title>VantoriX Business Card</title>
<link href="https://fonts.googleapis.com/css2?family=Lato:wght@400;700&display=swap" rel="stylesheet">
<style>
  :root {
    --navy: #012036;
    --cyan: #1ab7ea;
    --white: #ffffff;
    --backdrop: #dcdcdc;
    --pattern: #0b2c45;
  }
  html, body {
    margin: 0;
    padding: 0;
    width: 1200px;
    height: 1000px;
    overflow: hidden;
    background: var(--backdrop);
    font-family: "Lato", Arial, sans-serif;
  }
  .stage { position: relative; width: 1200px; height: 1000px; }
  .card {
    position: absolute;
    width: 700px;
    height: 420px;
    background: var(--navy);
    color: var(--white);
    overflow: hidden;
  }
  .card--front { left: 83px; top: 51px; }
  .card--back { left: 409px; top: 526px; }

  .wordmark {
    margin: 0;
    font-weight: 700;
    color: var(--white);
    letter-spacing: 3px;
    line-height: 1;
  }
  .card--front .wordmark {
    position: absolute;
    left: 0; right: 0;
    top: 178px;
    text-align: center;
    font-size: 74px;
  }
  .front-url {
    position: absolute;
    left: 0; right: 0;
    top: 366px;
    text-align: center;
    font-size: 15px;
    font-weight: 700;
  }
  .front-url .accent { color: var(--cyan); }

  .pattern-area {
    position: absolute;
    left: -20px; top: -60px;
    width: 290px; height: 290px;
    border-radius: 50%;
    background: radial-gradient(circle at 45% 45%, var(--pattern), rgba(11,44,69,0.4) 70%, rgba(11,44,69,0) 100%);
  }
  .brand-block {
    position: absolute;
    right: 41px;
    top: 62px;
    text-align: right;
  }
  .card--back .wordmark { font-size: 52px; }
  .tagline {
    margin: 6px 0 0;
    font-size: 17px;
    letter-spacing: 0.5px;
  }
  .contact-list {
    position: absolute;
    left: 43px;
    top: 303px;
    margin: 0; padding: 0;
    list-style: none;
    font-size: 15px;
    font-weight: 700;
  }
  .contact-list li {
    display: flex;
    align-items: center;
    height: 21px;
  }
  .contact-icon {
    width: 13px; height: 13px;
    margin-right: 7px;
    flex: none;
  }
  .contact-list .no-icon { padding-left: 20px; }
  .person {
    position: absolute;
    right: 42px;
    top: 318px;
    text-align: right;
  }
  .person-name {
    margin: 0;
    font-size: 21px;
    font-weight: 400;
    color: var(--cyan);
    line-height: 28px;
  }
  .person-credentials { margin: 0; font-size: 13px; line-height: 21px; }
  .person-role { margin: 0; font-size: 14px; font-weight: 700; line-height: 20px; }
  .accent-bar {
    position: absolute;
    left: 672px; top: 323px;
    width: 28px; height: 62px;
    background: var(--cyan);
  }
</style>
</head>
<body>
<div class="stage">
  <section class="card card--front">
    <p class="wordmark">VANTORIX</p>
    <p class="front-url">www.<span class="accent">vantorix</span>.global</p>
  </section>

  <section class="card card--back">
    <div class="pattern-area" role="img" aria-label="Faint decorative dotted sphere pattern"></div>
    <div class="brand-block">
      <p class="wordmark">VANTORIX</p>
      <p class="tagline">Safety &amp; Human Factors</p>
    </div>

    <ul class="contact-list">
      <li>
        <svg class="contact-icon" viewBox="0 0 16 16"><path fill="var(--cyan)" d="M3.5 1.5l2.5 0 1 3.5-1.7 1.2a9 9 0 0 0 4.5 4.5L11 9l3.5 1v2.5c0 1-1 2-2 2C6.5 14.5 1.5 9.5 1.5 3.5c0-1 1-2 2-2z"/></svg>
        +61 (0)400 555 018
      </li>
      <li>
        <svg class="contact-icon" viewBox="0 0 16 16"><rect x="1.5" y="3.5" width="13" height="10" rx="1" fill="var(--cyan)"/><path d="M2 4.5l6 4.5 6-4.5" stroke="var(--navy)" stroke-width="1.3" fill="none"/></svg>
        mholloway@vantorix.com.au
      </li>
      <li>
        <svg class="contact-icon" viewBox="0 0 16 16" fill="none" stroke="var(--cyan)" stroke-width="1.4"><circle cx="8" cy="8" r="6.3"/><ellipse cx="8" cy="8" rx="2.8" ry="6.3"/><path d="M1.7 8h12.6M2.8 4.8h10.4M2.8 11.2h10.4"/></svg>
        www.vantorix.com.au
      </li>
      <li class="no-icon">www.vantorix.global</li>
    </ul>

    <div class="person">
      <p class="person-name">Maren Holloway</p>
      <p class="person-credentials">BA (Hons), M Psych Org, M Tech Mgt (HF)</p>
      <p class="person-role">Managing Director</p>
    </div>
    <div class="accent-bar"></div>
  </section>
</div>
</body>
</html>
```